Business Card

The design you sent was fine. I just need the logo changed on one side. The back needs to have the text "Vell Marrow Group" next to the log and the words "Advice Acumen Advocacy" in the middle. The front logo needs to have the "Vell Marrow Advisory" logo attached

Colors

Designer to choose colors to be used in the design.

```html
<!DOCTYPE html>
<html lang="en">
<head>
<meta charset="utf-8">
<title>Vell Marrow Business Card</title>
<link href="https://fonts.googleapis.com/css2?family=Poppins:wght@400;500;600&family=Montserrat:wght@500;700&display=swap" rel="stylesheet">
<style>
  :root {
    --cyan: #00b5e2;
    --cyan-deep: #0aa3cc;
    --ink: #1d1d1f;
    --paper: #ffffff;
    --stage: #2a2a2c;
    --muted: #333333;
  }
  * { box-sizing: border-box; margin: 0; padding: 0; }
  html, body { width: 1200px; height: 880px; overflow: hidden; }
  body {
    background: var(--stage);
    font-family: "Poppins", sans-serif;
    color: var(--ink);
    position: relative;
  }
  .card {
    position: absolute;
    left: 280px;
    width: 640px;
    height: 366px;
    background: var(--paper);
    border-radius: 22px;
    overflow: hidden;
  }
  .card--back { top: 50px; }
  .card--front { top: 464px; }

  /* Back side */
  .values-band {
    position: absolute;
    top: 0; right: 0;
    width: 62px; height: 100%;
    background: var(--ink);
    border-left: 4px solid var(--cyan);
  }
  .values-band__text {
    position: absolute;
    top: 50%; left: 50%;
    transform: translate(-50%, -50%) rotate(90deg);
    white-space: nowrap;
    font-family: "Montserrat", sans-serif;
    font-weight: 500;
    font-size: 15px;
    letter-spacing: 3px;
    color: #ffffff;
  }
  .values-band__text strong { color: var(--cyan); font-weight: 700; }

  .group-brand {
    position: absolute;
    left: 48px; top: 168px;
  }
  .group-brand__row { display: flex; align-items: center; gap: 14px; }
  .group-brand__square {
    width: 44px; height: 44px;
    background: var(--ink);
  }
  .group-brand__name {
    font-weight: 600;
    font-size: 38px;
    line-height: 1;
    color: var(--ink);
  }
  .group-brand__tagline {
    margin: 8px 0 0 58px;
    font-size: 13px;
    color: var(--muted);
  }
  .group-brand__web {
    margin: 22px 0 0 58px;
    font-size: 14px;
    color: var(--ink);
  }
  .group-brand__web span { color: var(--cyan); }

  /* Front side */
  .accent-block {
    position: absolute;
    top: 0; right: 0;
    width: 100%; height: 100%;
  }
  .advisory-brand {
    position: absolute;
    left: 40px; top: 78px;
    width: 300px;
  }
  .advisory-brand__name {
    font-weight: 600;
    font-size: 48px;
    line-height: 1;
    color: var(--ink);
  }
  .advisory-brand__sub {
    display: flex; align-items: center; gap: 10px;
    margin-top: 8px;
  }
  .advisory-brand__sub::before,
  .advisory-brand__sub::after {
    content: ""; flex: 1; height: 1.5px; background: var(--ink);
  }
  .advisory-brand__sub span {
    font-family: "Montserrat", sans-serif;
    font-weight: 700;
    font-size: 17px;
    letter-spacing: 3px;
  }
  .advisory-brand__tagline {
    margin-top: 6px;
    font-size: 9.5px;
    font-weight: 500;
    color: var(--muted);
    border-top: 1.5px solid var(--ink);
    padding-top: 5px;
  }
  .holder {
    position: absolute;
    left: 40px; top: 222px;
  }
  .holder__name { font-weight: 600; font-size: 26px; line-height: 1.05; }
  .holder__role { font-size: 17px; color: var(--cyan); line-height: 1.2; }
  .contact-list {
    position: absolute;
    left: 40px; top: 290px;
    list-style: none;
  }
  .contact-list li {
    display: flex; align-items: center; gap: 10px;
    font-size: 15px; line-height: 22px;
    color: var(--ink);
  }
  .contact-list svg { width: 16px; height: 16px; flex: none; }
</style>
</head>
<body>

<section class="card card--back" aria-label="Card back">
  <div class="group-brand">
    <div class="group-brand__row">
      <div class="group-brand__square"></div>
      <div class="group-brand__name">Vell Marrow Group</div>
    </div>
    <p class="group-brand__tagline">Looking from outside the square</p>
    <p class="group-brand__web">www.<span>vellmarrow</span>.com</p>
  </div>
  <div class="values-band">
    <p class="values-band__text">ADVICE <strong>ACUMEN</strong> ADVOCACY</p>
  </div>
</section>

<section class="card card--front" aria-label="Card front">
  <svg class="accent-block" viewBox="0 0 640 366" aria-hidden="true">
    <path d="M415 0 H640 V366 H495 L470 300 L455 50 L415 40 Z" fill="var(--cyan)"/>
  </svg>
  <svg style="position:absolute;left:440px;top:30px;width:170px;height:230px" viewBox="0 0 170 230" role="img" aria-label="Light bulb illustration">
    <rect x="0" y="0" width="170" height="230" rx="18" fill="var(--cyan-deep)"/>
  </svg>

  <div class="advisory-brand">
    <div class="advisory-brand__name">Vell Marrow</div>
    <div class="advisory-brand__sub"><span>ADVISORY</span></div>
    <p class="advisory-brand__tagline">Exceptional Intellect providing Compelling Solutions</p>
  </div>

  <div class="holder">
    <p class="holder__name">Rowan Ellery</p>
    <p class="holder__role">Manager</p>
  </div>

  <ul class="contact-list">
    <li>
      <svg viewBox="0 0 16 16" aria-hidden="true"><circle cx="8" cy="8" r="8" fill="var(--cyan)"/><rect x="5.5" y="3.5" width="5" height="9" rx="1" fill="none" stroke="#fff" stroke-width="1.2"/></svg>
      +44 2040 118 372
    </li>
    <li>
      <svg viewBox="0 0 16 16" aria-hidden="true"><circle cx="8" cy="8" r="8" fill="var(--cyan)"/><rect x="4" y="5" width="8" height="6" fill="none" stroke="#fff" stroke-width="1.2"/><path d="M4 5 L8 8.5 L12 5" fill="none" stroke="#fff" stroke-width="1.2"/></svg>
      hello@vellmarrow.com
    </li>
    <li>
      <svg viewBox="0 0 16 16" aria-hidden="true"><circle cx="8" cy="8" r="8" fill="var(--cyan)"/><circle cx="8" cy="8" r="4.5" fill="none" stroke="#fff" stroke-width="1.1"/><path d="M3.5 8 H12.5 M8 3.5 C6 6 6 10 8 12.5 M8 3.5 C10 6 10 10 8 12.5" fill="none" stroke="#fff" stroke-width="1"/></svg>
      www.vellmarrow.com
    </li>
  </ul>
</section>

</body>
</html>
```